Supplement Package and Bottle Design*

We are a supplement company rebranding a number of product ranges for which we need a designer.

We will start with two products for joint health supplementation that are part of one range.

1. QUENTIL R58 Internal Oil Drops
The internal oil drop requires a design for the outer box and inside bottle label – see attached.

Front of box should include the following text:
- QUENTIL R58
- Internal Oil Drops
- Original formula from the oils of fresh Laurus nobilis L. leaves and Curcuma longa L. rhizomes
- Dilute before use
- Food supplement
- 100ml
- Some prominent icon/ graphics indicating use for joint health
- Brenuvel logo

2. QUENTIL M4 External Cream
The external cream only requires a design for the bottle label – see attached.
- QUENTIL M4
- External Cream
- Original formula from the oils of fresh Laurus nobilis L. leaves + 7 select ingredients
- 150ml
- Brenuvel logo

Overall design:
- Common design between both products (oil drops and cream)
Must appeal to a customer base of middle-age/ seniors
- Pharmaceutical product feel with touch of nature/ herbal remedy
- Design my convey a feeling of dependability, trust, effectiveness
- Premium product feel. These are very expensive products
- Design must be easy to adapt for new product ranges
- Use icons/ symbols to indicate health application, example: icon of knee to indicate use for joints
- "R58" and "M4" should be prominent to distinguish the products
- You have a choice of two Brenuvel logos. See attached.
- Primary colours: white and rgb(33, 136, 135)
- Designers can also consider some use of stamped gold/ silver for embellishments

Once a successful design/ feel has been chosen then exact dielines will be provided.

Target Market(s)

Seniors (65+ years old) with arthritis. Generally retired and affluent.

Industry/Entity Type

Health Product

Colors
33b8a4

Requirements
Must have
• As per project description.

Please creatively use a laurel wreath in the design. Either as a standalone element or multiple laurel wreaths in the background of the design. Can be vector or blended image.

As the supplements are made from bay leaves (laurel leaves) this subtle connection should be present.
Should not have
• Should not be cheap design and loud.

Premium design that conveys trust and pharmaceutical grade treatment with embellishments reminding that this is a natural/ herbal remedy product

```html
<!DOCTYPE html>
<html lang="en">
<head>
<meta charset="utf-8">
<title>QUENTIL R58 Internal Oil Drops – Bottle Label</title>
<link href="https://fonts.googleapis.com/css2?family=Tinos&family=Questrial&family=Montserrat:wght@500;600&display=swap" rel="stylesheet">
<style>
  :root {
    --teal: #218887;
    --teal-line: #4fb3ae;
    --white: #ffffff;
    --backdrop: #e4e5e9;
    --photo-grey: #d9d9d9;
    --photo-red: #e0555a;
  }
  html, body {
    margin: 0;
    width: 1200px;
    height: 900px;
    overflow: hidden;
    background: var(--backdrop);
  }
  .label {
    position: absolute;
    left: 341px;
    top: 40px;
    width: 422px;
    height: 668px;
    background: var(--teal);
    transform: scale(1.2275);
    transform-origin: top left;
    color: var(--white);
  }
  .label p { margin: 0; }
  .label > * { position: absolute; }
  .crest {
    left: 150px; top: 10px;
    width: 124px; height: 124px;
    border: 2px solid var(--teal-line);
    border-radius: 50%;
    box-sizing: border-box;
  }
  .joint-photo {
    left: 9px; top: 177px;
    width: 184px; height: 184px;
    border-radius: 50%;
    background: radial-gradient(circle at 45% 55%, var(--photo-red) 0%, #e99a9b 28%, var(--photo-grey) 55%, #8d8d8d 100%);
  }
  .range-name {
    right: 10px; top: 170px;
    font: 34px/1 "Tinos", serif;
    letter-spacing: -0.5px;
  }
  .product-code {
    right: 8px; top: 204px;
    font: 88px/1 "Tinos", serif;
    letter-spacing: -2px;
  }
  .product-type {
    right: 10px; top: 285px;
    font: 23px/1 "Questrial", sans-serif;
  }
  .formula {
    left: 216px; top: 319px;
    width: 200px;
    font: 12.5px/15px "Questrial", sans-serif;
  }
  .caps {
    left: 0; width: 100%;
    text-align: center;
    font: 600 15px/1 "Montserrat", sans-serif;
    letter-spacing: 4px;
  }
  .food-supplement { top: 389px; }
  .brand-band {
    left: 0; top: 409px;
    width: 100%; height: 141px;
    background: var(--white);
  }
  .brand-mark {
    position: absolute;
    left: 171px; top: 14px;
    width: 80px; height: 80px;
    border: 2.5px solid var(--teal);
    border-radius: 50%;
    box-sizing: border-box;
  }
  .brand-name {
    position: absolute;
    left: 0; top: 101px; width: 100%;
    text-align: center;
    color: var(--teal);
    font: 500 22px/1 "Montserrat", sans-serif;
    letter-spacing: 5px;
  }
  .dilute { top: 559px; }
  .volume {
    top: 624px;
    font: 500 28px/1 "Montserrat", sans-serif;
    letter-spacing: 6px;
  }
</style>
</head>
<body>
  <div class="label">
    <div class="crest"></div>
    <div class="joint-photo" role="img" aria-label="Photo of hands holding a knee with a red highlight showing joint pain"></div>
    <p class="range-name">QUENTIL</p>
    <p class="product-code">R58</p>
    <p class="product-type">Internal Oil Drops</p>
    <p class="formula">Original formula from the oils of fresh Laurus nobilis, L. leaves and Curcuma longa L. rhizomes</p>
    <p class="caps food-supplement">FOOD SUPPLEMENT</p>
    <div class="brand-band">
      <div class="brand-mark"></div>
      <p class="brand-name">BRENUVEL</p>
    </div>
    <p class="caps dilute">DILUTE BEFORE USE</p>
    <p class="caps volume">100ml</p>
  </div>
</body>
</html>
```